I need a website built for my modeling agency company.

On our website, a user can create a profile and we will submit it to thousands of modeling agents throughout the country.

In many cases, they will receive multiple offers from modeling agencies which allows them to pick and choose the contract that is best for them to launch their modeling career.

Some tag lines to consider using:

"Submit your profile to hundreds of modeling agents instantly!"

"Get found and become a star!"

We are: The Runway Guild.

Our Slogan: The World''s Largest Network of Fashion Models and Agents

What We Do: We are an agency with one of the largest networks of fashion professionals that are looking for new modeling talent. We host professional profiles for aspiring models, professional fashion models seeking work, modeling talent seekers, and top modeling agencies. We connect aspiring models with the top modeling agencies in the United States and abroad.

By submitting your FREE profile, you will be instantly introduced to the industry’s leading modeling agents. Within a few days, you could receive multiple, competing offers from modeling agencies that all want to launch your modeling career. Receiving multiple signing offers puts you in control of deciding which contract best suites you!

Reason: I've seen some good designs, but none that are 100% perfect. These are the ones that I like best so far (to give you some ideas): http://files.pixelvantor.com/img/501132/770214/770214_3391045_501132_image.jpg http://files.pixelvantor.com/img/501132/768531/768531_3397712_501132_image.jpg http://files.pixelvantor.com/img/501132/52817/52817_3394420_501132_image.jpg http://files.pixelvantor.com/img/501132/52817/52817_3389163_501132_image.jpg http://files.pixelvantor.com/img/501132/773906/773906_3390287_501132_image.jpg

Target Market(s)

Aspiring models (mostly female, but some male)

Industry/Entity Type

Modeling Agency

Colors

Designer to choose colors to be used in the design.

Requirements
Nice to have
• Somewhere in the top half of the page, I would like there to be a small form for the visitor to fill out. This form will look as follows:

Title: Instantly contact hundreds of modeling agents who are looking for new talent and could make you a star!
Fields: First Name*, Last Name*, Age, Zip Code, Email Address*, Daytime Phone, Evening Phone, Comments.

Then, there will be a "submit" button to proceed to next step of form. Just below the "submit" button, should be the following verbiage: "You will have the opportunity to upload photo(s) and provide other pertinent information in next step."

```html
<!DOCTYPE html>
<html lang="en">
<head>
<meta charset="utf-8">
<title>The Runway Guild</title>
<link href="https://fonts.googleapis.com/css2?family=Oswald:wght@400;500;600&family=Arimo:wght@400;700&display=swap" rel="stylesheet">
<style>
:root{
  --black:#000;
  --ink:#111;
  --charcoal:#222;
  --white:#fff;
  --red:#ee2a2f;
  --purple:#8e2a8f;
  --brown:#6b4a20;
  --blue:#2a9bd0;
  --field:#fff;
  --hero-light:#f5ece0;
  --hero-gold:#dcb173;
}
*{box-sizing:border-box;margin:0;padding:0}
html,body{width:853px;height:1200px;overflow:hidden;background:var(--white)}
body{font-family:'Arimo',Arial,sans-serif}
.page{position:relative;width:853px;height:1200px;overflow:hidden;background:var(--charcoal)}
.abs{position:absolute}

/* header */
.site-header{left:0;top:0;width:853px;height:103px;background:var(--black)}
.brand{left:102px;top:30px;color:var(--white)}
.brand-name{font-family:'Oswald',sans-serif;font-weight:500;font-size:25px;letter-spacing:1px;text-transform:uppercase;line-height:1}
.brand-tagline{font-family:'Arimo',sans-serif;font-size:7.5px;font-weight:700;margin-top:5px;white-space:nowrap}
.account-links{left:656px;top:17px;color:var(--white);font-family:'Oswald',sans-serif;font-size:13px;word-spacing:2px}
.main-nav{left:0;top:78px;height:25px;width:853px}
.main-nav a{position:absolute;top:0;height:25px;line-height:25px;color:var(--white);text-decoration:none;font-family:'Oswald',sans-serif;font-size:14px;text-transform:uppercase}
.main-nav a.active{background:var(--red);padding:0 6px}

/* hero */
.hero-photo{left:0;top:103px;width:853px;height:579px;
  background:linear-gradient(160deg,var(--hero-light) 0%,var(--hero-gold) 45%,var(--hero-gold) 60%,var(--hero-light) 100%)}
.feature{width:212px;height:212px;border-radius:50%;color:var(--white);text-align:center}
.feature-head{position:absolute;left:0;top:28px;width:212px;height:46px}
.feature-head svg{position:absolute}
.feature-title{position:absolute;font-family:'Oswald',sans-serif;font-weight:500;font-size:15px;text-transform:uppercase;top:13px}
.feature-text{position:absolute;left:18px;top:82px;width:176px;font-size:7px;line-height:15px;color:var(--ink)}
.who{left:94px;top:374px;background:var(--purple)}
.why{left:324px;top:374px;background:var(--brown)}
.what{left:548px;top:374px;background:var(--blue)}

/* signup form */
.signup{left:132px;top:606px;width:588px;height:336px;background:var(--black)}
.upload-band{left:16px;top:16px;width:556px;height:98px;background:var(--red)}
.upload-title{left:68px;top:8px;font-family:'Oswald',sans-serif;font-weight:500;font-size:16px;color:var(--black)}
.upload-sub{left:66px;top:30px;width:392px;text-align:center;font-family:'Oswald',sans-serif;font-weight:500;font-size:10px;line-height:11px;color:var(--black);text-transform:uppercase}
.file-field{left:72px;top:62px;width:337px;height:25px;background:var(--field);font-size:10px;font-style:italic;padding-left:30px;line-height:25px;text-transform:uppercase}
.upload-btn{left:422px;top:62px;width:107px;height:26px;background:var(--black);color:var(--white);font-family:'Oswald',sans-serif;font-weight:500;font-size:17px;text-align:center;line-height:26px}
.field-label{font-family:'Oswald',sans-serif;font-size:10px;color:var(--white);text-transform:uppercase;letter-spacing:.3px}
.field{background:var(--field);height:19px}
.submit-btn{left:344px;top:296px;width:106px;height:26px;background:var(--red);color:var(--white);font-family:'Oswald',sans-serif;font-weight:500;font-size:16px;text-align:center;line-height:26px}
.back-link{left:466px;top:309px;color:var(--white);font-size:7.5px;text-transform:uppercase}

/* gallery */
.gallery{left:94px;top:956px;width:667px;height:159px;background:var(--black);border-radius:3px}
.gallery-title{left:44px;top:10px;font-family:'Oswald',sans-serif;font-weight:500;font-size:17px;color:var(--red);text-transform:uppercase}
.thumb{top:42px;width:98px;height:94px}
.arrow{width:38px;height:38px;border-radius:50%;background:#2a2a2a;top:64px}

/* footer */
.site-footer{left:0;top:1128px;width:853px;height:72px;background:var(--black);color:var(--white)}
.follow{left:101px;top:30px;font-family:'Oswald',sans-serif;font-weight:500;font-size:12px}
.social{top:32px;font-size:9px;font-family:'Oswald',sans-serif}
.footer-nav{left:335px;top:30px;font-family:'Oswald',sans-serif;font-size:9px;word-spacing:8px;text-transform:uppercase}
.copyright{left:370px;top:48px;font-size:7px;text-transform:uppercase}
.footer-brand{left:616px;top:26px}
.footer-brand .brand-name{font-size:15px}
.footer-brand .brand-tagline{font-size:5px;margin-top:3px}
</style>
</head>
<body>
<div class="page">

  <header class="site-header abs">
    <div class="brand abs">
      <div class="brand-name">The Runway Guild</div>
      <div class="brand-tagline">The World's Largest Network of Fashion Models and Agents</div>
    </div>
    <div class="account-links abs">SIGN UP &nbsp;|&nbsp; LOG IN</div>
    <nav class="main-nav abs">
      <a class="active" href="#" style="left:460px">Home</a>
      <a href="#" style="left:517px">Models</a>
      <a href="#" style="left:577px">Casting</a>
      <a href="#" style="left:640px">Specials</a>
      <a href="#" style="left:706px">Contact</a>
    </nav>
  </header>

  <div class="hero-photo abs" role="img" aria-label="Hero photograph of a fashion model"></div>

  <section class="feature who abs">
    <div class="feature-head">
      <svg width="40" height="40" viewBox="0 0 40 40" style="left:18px;top:0">
        <polygon points="4,6 22,14 10,20" fill="#fff"/>
        <polygon points="26,4 34,28 20,18" fill="#fff"/>
        <polygon points="8,26 24,24 14,38" fill="#fff"/>
      </svg>
      <span class="feature-title" style="left:72px">Who We Are</span>
    </div>
    <p class="feature-text">We are an agency with one of the largest networks of fashion professionals that are looking for new modeling talent. We host professional profiles for aspiring models, professional fashion models seeking work, modeling talent seekers, and top modeling agencies. We connect aspiring models with the top modeling agencies in the United States and abroad.</p>
  </section>

  <section class="feature why abs">
    <div class="feature-head">
      <svg width="46" height="46" viewBox="0 0 46 46" style="left:44px;top:-4px">
        <polygon points="4,14 4,42 11,35 16,45 20,43 15,33 24,33" fill="#fff"/>
        <path d="M22,10 q0,-8 9,-8 q9,0 9,8 q0,5 -5,7 q-3,1 -3,5 v2" stroke="#fff" stroke-width="4" fill="none"/>
        <rect x="30" y="27" width="4" height="4" fill="#fff"/>
      </svg>
      <span class="feature-title" style="left:102px">Why Us?</span>
    </div>
    <p class="feature-text">We are an agency with one of the largest networks of fashion professionals that are looking for new modeling talent. We host professional profiles for aspiring models, professional fashion models seeking work, modeling talent seekers, and top modeling agencies. We connect aspiring models with the top modeling agencies in the United States and abroad.</p>
  </section>

  <section class="feature what abs">
    <div class="feature-head">
      <svg width="34" height="42" viewBox="0 0 34 42" style="left:44px;top:-6px">
        <rect x="3" y="6" width="28" height="34" rx="2" stroke="#fff" stroke-width="2.5" fill="none"/>
        <rect x="11" y="2" width="12" height="7" rx="1" fill="#fff"/>
        <polyline points="9,24 15,30 25,17" stroke="#fff" stroke-width="3" fill="none"/>
      </svg>
      <span class="feature-title" style="left:95px">What We Do</span>
    </div>
    <p class="feature-text">We are an agency with one of the largest networks of fashion professionals that are looking for new modeling talent. We host professional profiles for aspiring models, professional fashion models seeking work, modeling talent seekers, and top modeling agencies. We connect aspiring models with the top modeling agencies in the United States and abroad.</p>
  </section>

  <section class="signup abs">
    <div class="upload-band abs">
      <div class="upload-title abs">UPLOAD PHOTO</div>
      <div class="upload-sub abs">Instantly contact hundreds of modeling agents who are looking for new talent and could make you a star!</div>
      <div class="file-field abs">Select your file</div>
      <div class="upload-btn abs">UPLOAD</div>
    </div>

    <div class="field-label abs" style="left:65px;top:122px">Name:</div>
    <div class="field abs" style="left:52px;top:138px;width:235px"></div>
    <div class="field-label abs" style="left:65px;top:163px">Age:</div>
    <div class="field abs" style="left:52px;top:179px;width:235px"></div>
    <div class="field-label abs" style="left:65px;top:203px">Zip Code:</div>
    <div class="field abs" style="left:50px;top:220px;width:237px"></div>
    <div class="field-label abs" style="left:65px;top:244px">Email Address</div>
    <div class="field abs" style="left:50px;top:259px;width:237px"></div>
    <div class="field-label abs" style="left:65px;top:285px">Daytime Phone</div>
    <div class="field abs" style="left:50px;top:301px;width:237px"></div>

    <div class="field-label abs" style="left:356px;top:122px">Evening Phone:</div>
    <div class="field abs" style="left:344px;top:138px;width:201px"></div>
    <div class="field-label abs" style="left:356px;top:163px">Comments</div>
    <div class="field abs" style="left:344px;top:180px;width:201px;height:98px;border-radius:2px"></div>

    <div class="submit-btn abs">SUBMIT</div>
    <div class="back-link abs">Wait, go back</div>
  </section>

  <section class="gallery abs">
    <h2 class="gallery-title abs">Get Found and Become a Star</h2>
    <div class="arrow abs" style="left:1px">
      <svg width="38" height="38" viewBox="0 0 38 38"><polyline points="22,11 14,19 22,27" stroke="#fff" stroke-width="4" fill="none"/></svg>
    </div>
    <div class="thumb abs" style="left:55px;background:linear-gradient(135deg,#3c3a48,#b9a4b4)" role="img" aria-label="Model portrait"></div>
    <div class="thumb abs" style="left:169px;background:linear-gradient(135deg,#5a2a78,#b07fd0)" role="img" aria-label="Model portrait in purple tones"></div>
    <div class="thumb abs" style="left:282px;background:linear-gradient(135deg,#1c1c1c,#d9d4d0)" role="img" aria-label="Black and white model portrait"></div>
    <div class="thumb abs" style="left:397px;background:linear-gradient(135deg,#8a4a1c,#e9b27a)" role="img" aria-label="Model portrait in warm tones"></div>
    <div class="thumb abs" style="left:512px;background:linear-gradient(135deg,#3a0e18,#b45a6e)" role="img" aria-label="Model portrait in deep red tones"></div>
    <div class="arrow abs" style="left:627px">
      <svg width="38" height="38" viewBox="0 0 38 38"><polyline points="16,11 24,19 16,27" stroke="#fff" stroke-width="4" fill="none"/></svg>
    </div>
  </section>

  <footer class="site-footer abs">
    <div class="follow abs">FOLLOW US:</div>
    <div class="social abs" style="left:172px">Friendspace</div>
    <div class="social abs" style="left:232px">Chirpline</div>
    <nav class="footer-nav abs">Home Models Casting Specials Contact</nav>
    <div class="copyright abs">Copy-right@The Runway Guild</div>
    <div class="brand footer-brand abs">
      <div class="brand-name">The Runway Guild</div>
      <div class="brand-tagline">The World's Largest Network of Fashion Models and Agents</div>
    </div>
  </footer>

</div>
</body>
</html>
```